Wachsen statt welken - Flyer-Design für einen bahnbrechenden Workshop
Zielgruppe
Wir sind die Exzellenz in Faciliation - wir bringen Menschen so zusammen, dass etwas vollkommen Neues entsteht. Und wir bilden Menschen in dieser Kunst aus.
Aufgabenstellung
Mit unserem Workshop „Klar gestalten!“ begehen wir Neuland, für uns wie für unsere Kunden. Das wollen wir mit einem Flyer-Layout zum Ausdruck bringen.
Das Layout soll die bestehende KERO-CI weiterentwickeln. Insbesondere verzichten wir auf den im bisherigen CI abgelegten Bilder. Veränderbar sind sowohl Schriftarten als auch Layout-Elemente
Das Layout sollte generisch sein und die Grundlage für weitere Veranstaltungsflyer sein.
Uns schwebt ein reduziertes, konzentriertes Layout vor, bei dem der Inhalt wirken kann.
Zur Orientierung liegt der aktuelle Entwurf für unsere Homepage bei.
Die im Text angegebenen Inhalte müssen nicht alle im Flyer abgebildet werden. Der Designer/die Designerin kann eine Auswahl treffen der Inhalte, die sie für wichtig hält.
Zentral aber sind: Einführungspreis, Ort und Termin
Der Flyer ist ausschließlich zur digitalen Verteilung vorgesehen.

```html
<!DOCTYPE html>
<html lang="de">
<head>
<meta charset="utf-8">
<title>Wachsen statt welken – Workshop-Flyer</title>
<link rel="stylesheet" href="https://fonts.googleapis.com/css2?family=Open+Sans:wght@400;600;700;800&display=swap">
<style>
:root{
  --stage:#6a6a6a;
  --paper:#ffffff;
  --red:#e8424a;
  --maroon:#6b2433;
  --text:#7a3a4a;
  --muted:#9a6a76;
  --rule:#d9b7bd;
  --soft-red:#fbe3e4;
}
*{box-sizing:border-box;margin:0;padding:0}
html,body{width:1200px;height:900px;overflow:hidden;background:var(--stage);font-family:"Open Sans",Arial,sans-serif;color:var(--text)}
.stage{position:relative;width:1200px;height:900px}
.page{position:absolute;top:74px;width:530px;height:752px;background:var(--paper);border-top:7px solid var(--red);border-bottom:7px solid var(--maroon);overflow:hidden}
.page--front{left:54px}
.page--back{left:616px}
.page-label{position:absolute;top:848px;width:530px;text-align:center;color:#e8e8e8;font-size:11px}
.page-label--front{left:54px}.page-label--back{left:616px}
.brand-tile{position:absolute;top:1px;left:405px;width:83px;height:76px;background:var(--red);display:flex;align-items:center;justify-content:center;color:#fff;font-weight:700;font-size:16px;letter-spacing:1px}
.abs{position:absolute}

/* front */
.corner{position:absolute;width:20px;height:20px;border-color:var(--red);border-style:solid}
.corner--tl{left:62px;top:56px;border-width:6px 0 0 6px}
.corner--br{left:416px;top:420px;border-width:0 6px 6px 0}
.title-small{left:90px;top:72px;font-size:31px;font-weight:700;color:var(--red);line-height:1.1}
.title-big{left:88px;top:106px;font-size:60px;font-weight:800;color:var(--red);line-height:1.1;letter-spacing:-.5px}
.title-mid{left:90px;top:165px;font-size:38px;font-weight:700;color:var(--red);line-height:1.1}
.date{top:218px;text-align:right}
.date b{display:block;font-size:19px;color:var(--red);font-weight:700;line-height:1.1}
.date small{display:block;font-size:8px;font-weight:700;color:var(--maroon);margin-top:4px}
.date--a{left:98px}
.date--b{left:220px;text-align:left}
.date--b small{text-align:left}
.date-divider{left:210px;top:218px;width:1px;height:38px;background:var(--maroon)}
.dotted{left:93px;top:268px;width:338px;border-top:1px dashed var(--rule)}
.claim{left:93px;top:279px;font-size:16.5px;font-weight:700;color:var(--maroon)}
.claim-sub{left:93px;top:300px;font-size:11.5px;font-weight:700;color:var(--maroon)}
.copy{left:93px;width:345px;font-size:9.3px;line-height:1.42;color:var(--text)}
.topics-head{left:93px;top:449px;font-size:10px;font-weight:700;color:var(--maroon)}
.checklist{list-style:none}
.checklist li{position:relative;padding-left:13px}
.checklist li::before{content:"";position:absolute;left:0;width:7px;height:7px;border:1px solid var(--maroon);border-radius:1px}
.checklist li::after{content:"";position:absolute;left:2px;width:3px;height:2px;border-left:1px solid var(--maroon);border-bottom:1px solid var(--maroon);transform:rotate(-45deg)}
.topics{left:93px;top:469px;width:350px;font-size:9.3px;line-height:16.2px}
.topics li::before{top:4px}.topics li::after{top:6px}
.signup{left:75px;top:596px;font-size:9.5px;line-height:1.45;color:var(--maroon)}
.signup h4{font-size:10px;font-weight:700;margin-bottom:6px}
.signup .row{display:flex;align-items:center;gap:6px}
.signup .icon{width:9px;height:9px;background:var(--maroon);border-radius:1px;display:inline-block}
.signup strong{display:block;margin-top:4px;font-weight:700}
.price{left:236px;top:617px;width:217px;height:67px;display:flex}
.price-early{width:108px;background:var(--maroon);color:#fff;padding:5px 8px}
.price-early small{display:block;font-size:7px;font-weight:700}
.price-early b{display:block;font-size:34px;font-weight:600;line-height:1.05}
.price-early i{font-style:normal;font-size:7px;display:block;margin-top:-2px}
.price-intro{flex:1;border:1.5px solid var(--maroon);text-align:center;padding-top:5px;color:var(--maroon)}
.price-intro small{display:block;font-size:7.5px;font-weight:700}
.price-intro b{display:block;font-size:36px;font-weight:600;line-height:1.05}

/* back */
.schedule-title{left:43px;top:37px;font-size:14.5px;font-weight:700;color:var(--red)}
.day{left:43px;display:flex;align-items:center;gap:6px;font-size:11.5px;font-weight:700;color:var(--maroon)}
.day svg{width:16px;height:15px}
.day::after{content:"";display:block;height:1px;background:var(--maroon);margin-left:4px;margin-top:8px}
.day--fri::after{width:222px}
.day--sat::after,.day--sun::after{width:130px}
.small-copy{left:43px;width:230px;font-size:6.3px;line-height:1.7;color:var(--muted)}
.small-list{font-size:6.5px;line-height:13.7px;color:var(--muted)}
.small-list li::before{top:3px;left:0;width:6px;height:6px}
.small-list li::after{top:4.5px;left:1.5px}
.small-list--fri{left:59px}.small-list--fri li{padding-left:10px}
.small-list--sat{left:44px}.small-list--sat li{padding-left:18px}
.small-list--sun{left:44px}.small-list--sun li{padding-left:13px}
.diagram-title{width:200px;text-align:center;font-size:9px;font-weight:700;color:var(--red);line-height:1.3}
.diagram-area{border-radius:50%;background:radial-gradient(circle,var(--soft-red),#fff 75%)}
.cycle-title{width:140px;text-align:center;font-size:11px;font-weight:700;color:var(--red);line-height:1.2}
.trainer{left:281px;top:544px;width:200px;text-align:center;color:var(--maroon)}
.trainer h4{font-size:9px;font-weight:700}
.trainer .portrait{width:78px;height:78px;margin:10px auto 8px;border-radius:50%;border:3px solid var(--maroon);background:radial-gradient(circle at 50% 40%,#c9a594,#8a7566 60%,#5f6f4e)}
.trainer .name{font-size:11.5px;font-weight:600}
.trainer .role{font-size:9px}
.trainer .note{font-size:6.5px;color:var(--muted);margin-top:2px}
</style>
</head>
<body>
<div class="stage">

  <section class="page page--front">
    <div class="brand-tile">KERO</div>
    <span class="corner corner--tl"></span>
    <span class="corner corner--br"></span>

    <div class="abs title-small">Der Workshop</div>
    <div class="abs title-big">Wachsen</div>
    <div class="abs title-mid">statt welken</div>

    <div class="abs date date--a"><b>20-22 Sept.</b><small>in München</small></div>
    <div class="abs date-divider"></div>
    <div class="abs date date--b"><b>11-13 Okt.</b><small>in Köln</small></div>

    <div class="abs dotted"></div>

    <div class="abs claim">Wirksam werden! Klar gestalten!</div>
    <div class="abs claim-sub">Das Prinzip von „Wachsen statt welken“</div>

    <p class="abs copy" style="top:332px">Wie du Teil der großen Wende wirst und andere Menschen in ihre transformative Kraft begleitest.</p>
    <p class="abs copy" style="top:367px">Der Workshop „Wachsen statt welken“ stellt dir dafür den notwendigen Rahmen zur Verfügung. Er spannt den Bogen vom „Was“ (sollen wir tun?) zum „Wie“ (sollen wir handeln?) und bietet ein reiches Spektrum an Methoden und Ansätzen, um Menschen in ihre transformative Kraft zu bringen.</p>

    <div class="abs topics-head">Der Workshop beinhaltet unter anderem folgende Themen:</div>
    <ul class="abs checklist topics">
      <li>Warum wir mehr als nachhaltig sein können und müssen</li>
      <li>Die sieben Schritte zur Wirksamkeit</li>
      <li>Die vier Dimensionen des Erneuerns</li>
      <li>Den Anfang im Ende erkennen: Wir wir Projekte gut aufsetzen</li>
      <li>Räume des Wandels schaffen</li>
      <li>Körperübungen und Methoden zur Arbeit mit Blockaden, zur Zielklärung und zur Entscheidungsfindung</li>
    </ul>

    <div class="abs signup">
      <h4>Anmeldung:</h4>
      <div class="row"><span class="icon"></span>kontakt@kero-werkstatt.de</div>
      <div class="row"><span class="icon"></span>08131/5550247</div>
      <strong>KERO - Einfach anpacken</strong>
      Ahornweg 14<br>85990 Tannfeld
    </div>

    <div class="abs price">
      <div class="price-early"><small>für Fruhbucher (bis 31.8.):</small><b>600 €</b><i>inkl. Mwst.</i></div>
      <div class="price-intro"><small>Einführungspreis:</small><b>750 €</b></div>
    </div>
  </section>

  <section class="page page--back">
    <div class="brand-tile">KERO</div>

    <div class="abs schedule-title">Workshop-Ablauf :</div>

    <div class="abs day day--fri" style="top:66px">
      <svg viewBox="0 0 16 15"><rect x="1" y="2" width="14" height="12" fill="none" stroke="#6b2433" stroke-width="1.3"/><line x1="1" y1="5.5" x2="15" y2="5.5" stroke="#6b2433"/><line x1="4.5" y1="0" x2="4.5" y2="3.5" stroke="#6b2433" stroke-width="1.3"/><line x1="11.5" y1="0" x2="11.5" y2="3.5" stroke="#6b2433" stroke-width="1.3"/><line x1="4" y1="9" x2="12" y2="9" stroke="#6b2433"/><line x1="4" y1="11.5" x2="10" y2="11.5" stroke="#6b2433"/></svg>Freitag 17-21 Uhr
    </div>
    <p class="abs small-copy" style="top:90px;width:300px">Wir beginnen mit dem, wo wir gerade im Leben stehen. Wir lernen einanderkennen und erhalten Einblick in den Grundansatz von „Wachsen statt welken“ Wir begegnen unserer Angst und erfahren, wie wir sie fruchtbar machen können.</p>
    <ul class="abs checklist small-list small-list--fri" style="top:127px">
      <li>Begrüßung</li>
      <li>Schritt 1: Im Leben sein</li>
      <li>Wieso Nachhaltigkeit nicht ausreicht und inwiefern wir mehr bewirken können</li>
      <li>Schritt 2: Die Angst durchqueren</li>
      <li>Wie wir unsere Angst fruchtbar machen</li>
      <li>Abschluss &amp; Meditation</li>
    </ul>

    <div class="abs day day--sat" style="top:225px">
      <svg viewBox="0 0 16 15"><rect x="1" y="2" width="14" height="12" fill="none" stroke="#6b2433" stroke-width="1.3"/><line x1="1" y1="5.5" x2="15" y2="5.5" stroke="#6b2433"/><line x1="4.5" y1="0" x2="4.5" y2="3.5" stroke="#6b2433" stroke-width="1.3"/><line x1="11.5" y1="0" x2="11.5" y2="3.5" stroke="#6b2433" stroke-width="1.3"/><line x1="4" y1="9" x2="12" y2="9" stroke="#6b2433"/><line x1="4" y1="11.5" x2="10" y2="11.5" stroke="#6b2433"/></svg>Samstag
    </div>
    <p class="abs small-copy" style="top:249px">Der erste Tag ist den Methoden von „Wachsen statt welken“ gewidmet. Eine Morgenmeditation ermöglicht uns die Begegnung mit uns selbst. Wir erforschen die zentralen Ansätze von „Wachsen statt welken“ und erlernen die Kunst der Fragen, die ändern.</p>
    <p class="abs small-copy" style="top:297px">Wir öffnen für uns selbst Räume des Wandels und lernen, diese auch anderen Menschen zu eröffnen.</p>
    <ul class="abs checklist small-list small-list--sat" style="top:327px">
      <li>Begrüßung und Morgenmeditation</li>
      <li>Schritt 3: Der Frage lauschen</li>
      <li>Die Kunst des Fragens</li>
      <li>Die sieben Schritte zur Wirksamkeit</li>
      <li>Schritt 4: In Verbindung gehen</li>
      <li>Die vier Dimensionen des Erneuerns</li>
      <li>Schritt 5: Dem Impuls lauschen</li>
      <li>Räume des Wandels schaffen</li>
      <li>Die drei Aufgaben eines Facilitators</li>
      <li>Abschluss &amp; Meditation</li>
    </ul>

    <div class="abs day day--sun" style="top:478px">
      <svg viewBox="0 0 16 15"><rect x="1" y="2" width="14" height="12" fill="none" stroke="#6b2433" stroke-width="1.3"/><line x1="1" y1="5.5" x2="15" y2="5.5" stroke="#6b2433"/><line x1="4.5" y1="0" x2="4.5" y2="3.5" stroke="#6b2433" stroke-width="1.3"/><line x1="11.5" y1="0" x2="11.5" y2="3.5" stroke="#6b2433" stroke-width="1.3"/><line x1="4" y1="9" x2="12" y2="9" stroke="#6b2433"/><line x1="4" y1="11.5" x2="10" y2="11.5" stroke="#6b2433"/></svg>Sonntag
    </div>
    <p class="abs small-copy" style="top:503px">Der zweite Tag ist uns selbst und dem Wandel gewidmet. Beide Aspekte bedingen einander. Denn Veränderung vollzieht sich nur dann, wenn wir uns selbst verändern. Wir aber kann uns das gelingen? Und wieso schützen wir uns oftmals vor Veränderungen?</p>
    <p class="abs small-copy" style="top:551px">Wir erkennen die Bedeutung des Anfangs und wie wir lernen, unsere Arbeit richtig zu beginnen. Zum Abschluss unterstützen uns gegenseitig, den Transfer in den Alltag zu schaffen.</p>
    <ul class="abs checklist small-list small-list--sun" style="top:591px">
      <li>Begrüßung und Morgenmeditation</li>
      <li>Schritt 6: Den Anfang im Ende erkennen</li>
      <li>Schritt 7: Wirksam werden</li>
      <li>Das Zentrum: die Arbeit mit sich selbst</li>
      <li>Der Schutz vor Veränderungen: Wandel wirklich verstehen</li>
      <li>Abschluss</li>
    </ul>

    <div class="abs diagram-title" style="left:281px;top:121px">Die Vier Dimension der<br>Erneuerung</div>
    <div class="abs diagram-area" style="left:306px;top:153px;width:150px;height:150px" role="img" aria-label="Schaubild der vier Dimensionen der Erneuerung"></div>

    <div class="abs diagram-area" style="left:286px;top:324px;width:190px;height:190px" role="img" aria-label="Kreisschaubild der sieben Schritte der Wirksamkeit"></div>
    <div class="abs cycle-title" style="left:311px;top:401px">Die sieben Schritte der Wirksamkeit</div>

    <div class="abs trainer">
      <h4>Dein Trainer :</h4>
      <div class="portrait" role="img" aria-label="Porträtfoto des Trainers"></div>
      <div class="name">Jonas Wendler,</div>
      <div class="role">Begründer von Wachsen statt Welken.</div>
      <div class="note">Begeisteter und inspirierender Facilitator.</div>
    </div>
  </section>

  <div class="page-label page-label--front">Pg.1</div>
  <div class="page-label page-label--back">Pg.2</div>
</div>
</body>
</html>
```